New Business Card Design

We would like to refresh our business cards and make them look better. We are an IT company specialising in Cloud Services, IT Managed Services, software and hardware. I have attached a PSD of our current design. Also attached our logo.
Updates

I have uploaded all new logos in EPS format.

Can you please edit all designs to include a job title for Marcus Hale, eg. General Manager

Industry/Entity Type

Software

Colors
ffffff

Requirements
Must have
• Please use white background.
Should not have
• Black background

```html
<!DOCTYPE html>
<html lang="en">
<head>
<meta charset="utf-8">
<title>Meridian Systems – Business Card</title>
<link href="https://fonts.googleapis.com/css2?family=Open+Sans:wght@300;400;600&family=Oswald:wght@500&display=swap" rel="stylesheet">
<style>
  :root {
    --stage: #ecebe8;
    --brand-red: #c8372b;
    --brand-red-light: #d9473a;
    --brand-red-dark: #b02b21;
    --card-white: #ffffff;
    --card-fog: #eef0f2;
    --steel: #8e9aa6;
    --steel-dark: #6f7c89;
    --ink: #2b2f33;
    --ink-soft: #4a4f55;
  }
  * { box-sizing: border-box; margin: 0; padding: 0; }
  html, body {
    width: 1200px;
    height: 1024px;
    overflow: hidden;
    background: var(--stage);
    font-family: "Open Sans", Arial, sans-serif;
  }
  .stage {
    position: relative;
    width: 1200px;
    height: 1024px;
  }
  .card {
    position: absolute;
    left: 250px;
    width: 700px;
    height: 400px;
    border-radius: 6px;
    overflow: hidden;
    box-shadow: 0 14px 34px rgba(0,0,0,0.16);
  }

  /* Front */
  .card-front {
    top: 72px;
    background: radial-gradient(circle at 40% 35%, var(--brand-red-light), var(--brand-red) 55%, var(--brand-red-dark));
    display: flex;
    align-items: center;
    justify-content: center;
  }
  .front-wordmark {
    display: flex;
    align-items: center;
    gap: 26px;
  }
  .front-wordmark .mark-dot {
    width: 92px;
    height: 92px;
    border-radius: 50%;
    background: var(--card-white);
  }
  .front-wordmark .brand-name {
    color: var(--card-white);
    font-weight: 300;
    font-size: 54px;
    letter-spacing: 4px;
    line-height: 1;
  }

  /* Back */
  .card-back {
    top: 552px;
    background: linear-gradient(135deg, var(--card-white) 0%, var(--card-fog) 100%);
  }
  .back-swoosh {
    position: absolute;
    left: 0;
    bottom: 0;
    width: 700px;
    height: 400px;
  }
  .back-brand {
    position: absolute;
    left: 44px;
    top: 70px;
    width: 250px;
    display: flex;
    align-items: center;
    gap: 16px;
  }
  .back-brand .mark-dot {
    flex: none;
    width: 56px;
    height: 56px;
    border-radius: 50%;
    background: var(--brand-red);
  }
  .back-brand .brand-name {
    color: var(--ink-soft);
    font-weight: 300;
    font-size: 30px;
    letter-spacing: 2px;
    line-height: 1.1;
  }
  .divider {
    position: absolute;
    left: 322px;
    top: 46px;
    width: 1px;
    height: 200px;
    background: var(--ink-soft);
    opacity: 0.6;
  }
  .contact-block {
    position: absolute;
    left: 352px;
    top: 40px;
  }
  .person-name {
    font-family: "Oswald", "Arial Narrow", sans-serif;
    font-weight: 500;
    font-size: 36px;
    color: var(--ink);
    line-height: 1.1;
  }
  .job-title {
    font-size: 15px;
    font-weight: 600;
    color: var(--brand-red);
    letter-spacing: 1px;
    text-transform: uppercase;
    margin: 4px 0 14px;
  }
  .contact-list { list-style: none; }
  .contact-list li {
    display: flex;
    align-items: center;
    gap: 12px;
    font-size: 16px;
    color: var(--ink-soft);
    height: 30px;
  }
  .contact-icon {
    width: 22px;
    height: 22px;
    flex: none;
  }
</style>
</head>
<body>
<main class="stage">

  <section class="card card-front" aria-label="Business card front">
    <div class="front-wordmark">
      <span class="mark-dot"></span>
      <span class="brand-name">Meridian Systems</span>
    </div>
  </section>

  <section class="card card-back" aria-label="Business card back">
    <svg class="back-swoosh" viewBox="0 0 700 400" aria-hidden="true">
      <path d="M0 250 C 160 360, 420 360, 700 330 L700 400 L0 400 Z" fill="var(--steel)"/>
      <path d="M0 290 C 170 380, 430 378, 700 362 L700 400 L0 400 Z" fill="var(--card-white)"/>
      <path d="M0 318 C 180 392, 440 390, 700 378 L700 400 L0 400 Z" fill="var(--brand-red)"/>
    </svg>

    <div class="back-brand">
      <span class="mark-dot"></span>
      <span class="brand-name">Meridian Systems</span>
    </div>

    <div class="divider"></div>

    <div class="contact-block">
      <h1 class="person-name">Marcus Hale</h1>
      <p class="job-title">General Manager</p>
      <ul class="contact-list">
        <li>
          <svg class="contact-icon" viewBox="0 0 22 22" aria-hidden="true">
            <circle cx="11" cy="11" r="11" fill="var(--brand-red)"/>
            <path d="M7.5 6.5 l2 -0.5 1 2.5 -1.2 1 a6 6 0 0 0 3.2 3.2 l1 -1.2 2.5 1 -0.5 2 c-4.5 0.3 -8.3 -3.5 -8 -8 z" fill="#fff"/>
          </svg>
          07 5550 1234
        </li>
        <li>
          <svg class="contact-icon" viewBox="0 0 22 22" aria-hidden="true">
            <circle cx="11" cy="11" r="11" fill="var(--brand-red)"/>
            <rect x="8" y="5" width="6" height="12" rx="1" fill="#fff"/>
            <rect x="9" y="7" width="4" height="7" fill="var(--brand-red)"/>
          </svg>
          0400 555 019
        </li>
        <li>
          <svg class="contact-icon" viewBox="0 0 22 22" aria-hidden="true">
            <circle cx="11" cy="11" r="11" fill="var(--brand-red)"/>
            <rect x="5.5" y="7" width="11" height="8" rx="1" fill="#fff"/>
            <path d="M5.5 7.5 L11 11.5 L16.5 7.5" stroke="var(--brand-red)" stroke-width="1.2" fill="none"/>
          </svg>
          mhale@meridiansys.com.au
        </li>
        <li>
          <svg class="contact-icon" viewBox="0 0 22 22" aria-hidden="true">
            <circle cx="11" cy="11" r="11" fill="var(--brand-red)"/>
            <circle cx="11" cy="11" r="5.5" stroke="#fff" stroke-width="1.3" fill="none"/>
            <path d="M5.5 11 H16.5 M11 5.5 C 8.5 8, 8.5 14, 11 16.5 M11 5.5 C 13.5 8, 13.5 14, 11 16.5" stroke="#fff" stroke-width="1.1" fill="none"/>
          </svg>
          www.meridiansys.com.au
        </li>
      </ul>
    </div>
  </section>

</main>
</body>
</html>
```